South Carolina Bridal and Formal Wear Store

We want The Gown Parlor of Ashcombe website to feel luxurious, elegant, welcoming, and approachable—without feeling overpriced or intimidating. The site should immediately show that we are a full-service bridal and formal wear destination, offering bridal gowns, prom, mothers’ dresses, tuxedos and suits, accessories, and more. We want beautiful, high-end imagery and a clean, modern design while still reflecting the warm, personal experience customers receive when they walk into our boutique. Most importantly, the website should be easy to shop and navigate, allowing customers to browse our collections, see what we offer, understand price ranges, book appointments, and feel excited and comfortable choosing The Gown Parlor of Ashcombe for all of their special-event needs.

Target Market(s)

Women ages 18-50. Brides, engaged women, mothers of the occasion

Industry/Entity Type

Bridal and Formal Wear

Coding

Coded - Design and coding required

Number of Pages Required

5+ page

Font styles to use
Sans Serif

Colors

Designer to choose colors to be used in the design.

Requirements
Must have
• Appointment area, about us staff area, what we offer and designers our logo
Nice to have
• Modern Southern Luxury: Clean, elegant, and upscale with soft neutral tones, beautiful bridal photography, and a warm Lowcountry feel.
Should not have
• pricing

```html
<!DOCTYPE html>
<html lang="en">
<head>
<meta charset="utf-8">
<title>Contact — The Gown Parlor of Ashcombe</title>
<link href="https://fonts.googleapis.com/css2?family=Playfair+Display:wght@400;600;700&family=Cormorant+Garamond:ital,wght@1,500&family=Lato:wght@400;700&display=swap" rel="stylesheet">
<style>
:root{
  --burgundy:#5c1f2c;
  --burgundy-deep:#571c29;
  --gold:#c39a62;
  --cream:#faf5f1;
  --field:#fbf4f0;
  --field-line:#ecd2cd;
  --ink:#3b2a2d;
  --white:#ffffff;
}
*{box-sizing:border-box;margin:0;padding:0}
html,body{width:723px;height:1200px;overflow:hidden;background:var(--white)}
body{font-family:'Lato',sans-serif;color:var(--ink);position:relative}
.page{position:relative;width:723px;height:1200px;overflow:hidden}
.abs{position:absolute}
.script{font-family:'Cormorant Garamond',serif;font-style:italic;font-weight:500;color:var(--gold)}
.divider{display:flex;align-items:center;justify-content:center;gap:5px}
.divider i{display:block;width:22px;height:0.6px;background:var(--gold)}
.divider b{display:block;width:3.5px;height:3.5px;background:var(--gold);transform:rotate(45deg)}

/* top bar */
.topbar{left:0;top:0;width:723px;height:12px;background:var(--burgundy);color:#ead7d2;font-size:4.4px;border-bottom:0.6px solid var(--gold)}
.topbar span{position:absolute;top:3.5px;white-space:nowrap}

/* header */
.header{left:0;top:12px;width:723px;height:45px;background:var(--cream);border-bottom:0.6px solid #d8c2a0}
.nav a{position:absolute;top:20px;font-family:'Playfair Display',serif;font-size:6px;letter-spacing:.3px;color:var(--burgundy);text-decoration:none}
.nav a.active{color:#8b5a3e;border-bottom:0.6px solid var(--gold);padding-bottom:1.5px}
.brand{position:absolute;left:295px;top:12px;width:132px;text-align:center;font-family:'Playfair Display',serif;font-weight:400;font-size:9.2px;line-height:10.5px;color:var(--burgundy)}
.btn{display:flex;align-items:center;justify-content:center;background:var(--burgundy);color:var(--white);font-family:'Playfair Display',serif;font-weight:700;font-size:6.2px;white-space:nowrap}
.header .btn{position:absolute;left:502px;top:14px;width:81px;height:18px;box-shadow:0 1px 3px rgba(0,0,0,.2)}

/* hero */
.hero{left:0;top:57px;width:723px;height:285px;background:linear-gradient(180deg,#7b4a4a 0%,#8d6166 45%,#a27b86 100%)}
.hero-copy{position:absolute;left:0;top:0;width:723px;text-align:center;color:var(--white)}
.hero .script{position:absolute;top:90px;width:100%;font-size:7.5px}
.hero h1{position:absolute;top:108px;width:100%;font-family:'Playfair Display',serif;font-weight:600;font-size:23.5px;line-height:24px}
.hero .divider{position:absolute;top:166px;width:100%}
.hero p{position:absolute;top:178px;left:260px;width:203px;font-size:6px;line-height:9px}

/* info card */
.info{left:160px;top:378px;width:404px;height:89px;background:var(--burgundy);border-radius:2px;box-shadow:0 3px 8px rgba(60,20,30,.25);color:#f3e6e3}
.info-col{position:absolute;top:18px;width:130px;text-align:center;font-size:6px;line-height:10px}
.info-col .script{font-size:7px;display:block;line-height:9px}
.info-col .divider{margin:2px 0 5px}
.info-col a{color:#f3e6e3;text-decoration:underline}
.hours{display:grid;grid-template-columns:1fr 1fr;width:70px;margin:0 auto;font-size:5.3px;text-align:left}

/* map + form */
.map{left:160px;top:488px;width:152px;height:282px;background:linear-gradient(170deg,#c9e3ec 0%,#e4eddc 40%,#e9f0e1 100%);border-top:1px solid #d9c19a;border-bottom:1px solid #d9c19a}
.form{left:327px;top:490px;width:237px;height:282px}
.form-intro{position:absolute;left:0;top:0;width:237px}
.form .script{display:block;font-size:7.5px;line-height:10px}
.form h2{margin-top:6px;font-family:'Playfair Display',serif;font-weight:400;font-size:11.4px;line-height:15px;white-space:nowrap;color:var(--burgundy)}
.form .divider{justify-content:flex-start;margin-top:6px}
.form p{margin-top:9px;font-size:5.6px;line-height:8px;white-space:nowrap}
.label{position:absolute;font-size:4.3px;line-height:5px;letter-spacing:.6px;color:#6b5659;white-space:nowrap}
.field{position:absolute;background:var(--field);border:0.6px solid var(--field-line);font-size:5.6px;color:var(--ink);display:flex;align-items:center;padding:0 6px;justify-content:space-between}
.form .btn{position:absolute;left:0;top:259px;width:70px;height:21px;font-size:6.2px;box-shadow:0 2px 4px rgba(0,0,0,.2)}

/* cta */
.cta{left:0;top:806px;width:723px;height:166px;background:var(--burgundy);text-align:center;color:var(--white)}
.cta .script{position:absolute;top:32px;width:100%;font-size:7.5px}
.cta h2{position:absolute;top:50px;width:100%;font-family:'Playfair Display',serif;font-weight:600;font-size:19px;line-height:22px}
.cta .divider{position:absolute;top:103px;width:100%}
.cta .link{position:absolute;top:121px;width:100%;font-family:'Playfair Display',serif;font-weight:700;font-size:6.4px}

/* footer */
.footer{left:0;top:972px;width:723px;height:228px;background:var(--burgundy-deep);border-top:0.6px solid #6e3340;color:#e8d7d3;text-align:center}
.footer .brand{left:296px;top:30px;width:131px;color:var(--white);font-size:9.2px}
.footer .tagline{position:absolute;top:60px;left:285px;width:153px;font-size:5px;line-height:8.5px}
.footer .divider{position:absolute;top:94px;width:100%}
.fcol{position:absolute;top:113px;width:110px;font-size:5px;line-height:7.5px}
.fcol .script{display:block;font-size:6.3px;margin-bottom:7px}
.fcol div{margin-bottom:3.8px}
.fhours{display:grid;grid-template-columns:1fr 1fr;width:62px;margin:0 auto;text-align:left;row-gap:3px}
.legal{position:absolute;left:0;top:204px;width:723px;height:24px;border-top:0.6px solid #6e3340;font-size:4.2px}
.legal span{position:absolute;top:10px;white-space:nowrap}
</style>
</head>
<body>
<div class="page">

  <div class="abs topbar">
    <span style="left:136px">&#9633; Wed – Sat, 10am – 6pm · Ashcombe, SC</span>
    <span style="left:435px">&#9742; 843-555-0142</span>
    <span style="left:483px">&#9993; appointments@thegownparlorofashcombe.com</span>
  </div>

  <header class="abs header">
    <nav class="nav">
      <a style="left:170px">HOME</a>
      <a style="left:207px">ABOUT</a>
      <a style="left:246px">COLLECTIONS</a>
      <a style="left:434px">FAQ</a>
      <a class="active" style="left:464px">CONTACT</a>
    </nav>
    <div class="brand">The Gown Parlor<br>of Ashcombe</div>
    <div class="btn">Book an Appointment</div>
  </header>

  <section class="abs hero" role="img" aria-label="Photo of a bride and groom walking hand in hand through guests tossing rose petals">
    <div class="hero-copy">
      <div class="script">Contact</div>
      <h1>We'd love to hear from<br>you</h1>
      <div class="divider"><i></i><b></b><i></i></div>
      <p>Visit our boutique in the heart of Ashcombe, or reach out any time — we're happy to help.</p>
    </div>
  </section>

  <section class="abs info">
    <div class="info-col" style="left:10px">
      <span class="script">Visit the Boutique</span>
      <div class="divider"><i></i><b></b><i></i></div>
      418 Marsh Hollow Lane, Suite 7<br>Ashcombe, SC 29940
    </div>
    <div class="info-col" style="left:137px">
      <span class="script">Reach Us</span>
      <div class="divider"><i></i><b></b><i></i></div>
      <a>843-555-0142</a><br><a>appointments@thegownparlorofashcombe.com</a>
    </div>
    <div class="info-col" style="left:263px">
      <span class="script">Store Hours</span>
      <div class="divider"><i></i><b></b><i></i></div>
      <div class="hours"><span>Sun – Tue</span><span style="text-align:right">Closed</span><span>Wed – Sat</span><span style="text-align:right">10am – 6pm</span></div>
    </div>
  </section>

  <div class="abs map" role="img" aria-label="Street map showing the boutique location"></div>

  <section class="abs form">
    <div class="form-intro">
      <span class="script">Get In Touch</span>
      <h2>Request an Appointment or Ask a Question</h2>
      <div class="divider"><i></i><b></b><i></i></div>
      <p>Fill out the form below and our team will follow up to confirm your appointment details.</p>
    </div>

    <span class="label" style="left:0;top:75px">FULL NAME</span>
    <div class="field" style="left:0;top:82px;width:114px;height:19px"></div>
    <span class="label" style="left:123px;top:75px">EMAIL</span>
    <div class="field" style="left:123px;top:82px;width:114px;height:19px"></div>

    <span class="label" style="left:0;top:112px">PHONE</span>
    <div class="field" style="left:0;top:119px;width:114px;height:19px"></div>
    <span class="label" style="left:123px;top:112px">APPOINTMENT TYPE</span>
    <div class="field" style="left:123px;top:119px;width:114px;height:18px"><span>VIP Bridal Appointment</span><span style="font-size:5px">&#8964;</span></div>

    <span class="label" style="left:0;top:149px">PREFERRED DATE</span>
    <div class="field" style="left:0;top:156px;width:237px;height:19px"><span>dd-mm-yyyy</span><span>&#9635;</span></div>

    <span class="label" style="left:0;top:186px">MESSAGE</span>
    <div class="field" style="left:0;top:193px;width:237px;height:55px"></div>

    <div class="btn">Send Request</div>
  </section>

  <section class="abs cta">
    <div class="script">We Can't Wait to Meet You</div>
    <h2>Ready to say yes to the<br>dress?</h2>
    <div class="divider"><i></i><b></b><i></i></div>
    <div class="link">Book an Appointment</div>
  </section>

  <footer class="abs footer">
    <div class="brand">The Gown Parlor<br>of Ashcombe</div>
    <div class="tagline">A full-service bridal &amp; formal wear boutique bringing timeless Southern elegance to Ashcombe, SC.</div>
    <div class="divider"><i></i><b></b><i></i></div>
    <div class="fcol" style="left:215px">
      <span class="script">Explore</span>
      <div>About Us</div><div>Collections</div><div>Appointments</div><div>FAQ</div>
    </div>
    <div class="fcol" style="left:306px">
      <span class="script">Visit Us</span>
      <div>418 Marsh Hollow Lane, Suite 7<br>Ashcombe, SC 29940</div>
      <div>843-555-0142</div>
      <div>appointments@thegownparlorof<br>ashcombe.com</div>
    </div>
    <div class="fcol" style="left:398px">
      <span class="script">Store Hours</span>
      <div class="fhours"><span>Sun – Tue</span><span style="text-align:right">Closed</span><span>Wed – Sat</span><span style="text-align:right">10am – 6pm</span></div>
    </div>
    <div class="legal">
      <span style="left:136px">© 2026 The Gown Parlor of Ashcombe. All rights reserved.</span>
      <span style="right:136px">Bridal · Tuxedos · Formal Wear · Ashcombe, SC</span>
    </div>
  </footer>

</div>
</body>
</html>
```